Veterinary Hospital Brochure - 2 Drafts - 1 Normal and 1 Fun.

Meadowbrook Pet Hospital needs a brochure to promote our veterinary hospital. These will be delivered to local mailboxes. I would like to see atleast 2 submissions from each designer.
One submission conservative and A4 folded DL and another submission more radical and interesting with innovative folding or crazy concepts. Maybe the brochure could be designed to fold into a dog house ?
I want at least one version to be VERY SIMPLE AND INTIMATE.
Our existing website is here: http://furlane.example/ and our new website will look like this: http://trial4.pagemint.example/#home
Please use colors and images from the new website, and information from the old website. The heading font used in the new site is Qorvatype - Otter Tilt Sketchline
I want the brochure to be simple and engaging on first view, and then provide the opportunity to find more information if desired. The brochure needs to be captivating on the outside so people don't throw it away immediately.

We will soon need letterhead, flags, pens, business cards, signs and vouchers so there is the opportunity for more work for the successful designer.

Target Market(s)

Women 25 to 44

Industry/Entity Type

Veterinary

Contact Information for Business Card

Meadowbrook Pet Hospital
14 Marlow Crescent
Tamsworth Vale
NSW 2417
Phone: 02 61938205
Emergency: 0417360592
Fax: 02 83159462
www.meadowbrookvets.example
contact@meadowbrookvets.example

Font styles to use
Script

Requirements
Must have
• Colors from the new website: http://meadowbrookvets.example/ and new logo.
• Information from the old website: http://furlane.example/
• 2 drafts - A normal A4 folded DL flyer and an interesting crazy design.
Nice to have
• VERY SIMPLE
• Subdued
• Intimate
Should not have
• Intense colours
• Red

```html
<!DOCTYPE html>
<html lang="en">
<head>
<meta charset="utf-8">
<title>Meadowbrook Pet Hospital – Brochure Inside Spread</title>
<link href="https://fonts.googleapis.com/css2?family=PT+Sans:wght@400;700&display=swap" rel="stylesheet">
<style>
  :root{
    --orange:#ee7d44;
    --orange-deep:#e8692f;
    --green:#7ea052;
    --green-dark:#5f8a2e;
    --ink:#3d3d3d;
    --paper:#ffffff;
    --backdrop:#e6e6e6;
  }
  *{box-sizing:border-box;margin:0;padding:0}
  html,body{width:1200px;height:800px;overflow:hidden;background:var(--backdrop);font-family:"PT Sans",sans-serif}
  .spread{position:absolute;left:50px;top:11px;width:1100px;height:778px;background:var(--paper);overflow:hidden;box-shadow:0 4px 14px rgba(0,0,0,.12)}
  .spread-art{position:absolute;inset:0}
  .fold{position:absolute;top:0;bottom:0;width:1px;background:rgba(0,0,0,.06)}
  .panel-heading{color:var(--orange);font-weight:700;text-transform:uppercase;letter-spacing:.3px}
  .about{position:absolute;left:32px;top:34px;width:305px;color:var(--ink);font-size:14.5px;line-height:1.22}
  .about .panel-heading{font-size:22px;padding-bottom:4px;border-bottom:1px solid var(--green);margin-bottom:10px;width:110px}
  .about p{text-align:justify;margin-bottom:16px}
  .about .web{display:block;color:var(--green-dark);font-weight:700;font-size:15px;margin-top:-14px}
  .services{position:absolute;left:392px;top:300px;width:360px;color:#fff}
  .services .panel-heading{color:#fff;font-size:21px;text-align:center;margin-bottom:12px}
  .service-cols{display:flex;gap:14px}
  .service-list{list-style:none;font-size:14.5px;line-height:1.78}
  .service-list li{display:flex;align-items:center;gap:8px;white-space:nowrap}
  .paw{width:13px;height:13px;fill:#fff;flex:none}
  .classes{position:absolute;left:778px;top:220px;width:300px;color:#fff;font-size:14px;line-height:1.3}
  .classes .panel-heading{color:#fff;font-size:21px;padding-bottom:4px;border-bottom:1px solid rgba(255,255,255,.8);margin-bottom:8px}
  .emergency-line{position:absolute;left:0;top:716px;width:740px;height:46px;display:flex;align-items:center;color:#fff;font-size:19px;padding-left:26px;white-space:nowrap}
  .emergency-line strong{font-size:21px;letter-spacing:.5px;margin-left:6px}
</style>
</head>
<body>
<svg width="0" height="0" style="position:absolute">
  <symbol id="paw" viewBox="0 0 20 20">
    <circle cx="4" cy="8" r="2.3"/><circle cx="8" cy="4" r="2.4"/><circle cx="13" cy="4" r="2.4"/><circle cx="17" cy="8" r="2.3"/>
    <ellipse cx="10.5" cy="13.5" rx="5" ry="4.2"/>
  </symbol>
  <linearGradient id="tone-hug" x1="0" y1="0" x2="1" y2="1"><stop offset="0" stop-color="#cfd7d8"/><stop offset=".45" stop-color="#d9b59a"/><stop offset="1" stop-color="#3e3630"/></linearGradient>
  <linearGradient id="tone-pair" x1="0" y1="0" x2="1" y2="1"><stop offset="0" stop-color="#ffffff"/><stop offset=".5" stop-color="#d9a870"/><stop offset="1" stop-color="#c27c45"/></linearGradient>
  <linearGradient id="tone-exam" x1="0" y1="0" x2="1" y2="1"><stop offset="0" stop-color="#e7e2dc"/><stop offset=".5" stop-color="#a98766"/><stop offset="1" stop-color="#3b3c4a"/></linearGradient>
  <linearGradient id="tone-pup" x1="0" y1="0" x2="1" y2="1"><stop offset="0" stop-color="#f4f1ec"/><stop offset="1" stop-color="#8a6b4f"/></linearGradient>
  <linearGradient id="orange-fade" x1="0" y1="0" x2="0" y2="1"><stop offset="0" stop-color="#f18a54"/><stop offset="1" stop-color="#ea7138"/></linearGradient>
</svg>

<main class="spread">
  <svg class="spread-art" viewBox="0 0 1100 778" width="1100" height="778">
    <path d="M367,0 H1100 V778 H0 V650 C140,650 300,630 336,560 C362,500 367,420 367,300 Z" fill="url(#orange-fade)"/>
    <path d="M0,650 C140,650 300,630 336,560 C362,500 367,420 367,300" fill="none" stroke="var(--green)" stroke-width="6"/>
    <g role="img" aria-label="Photo of a golden retriever lying beside a ginger cat">
      <path d="M40,350 C120,340 300,360 340,420 C360,470 345,560 320,610 C240,660 100,660 40,640 Z" fill="url(#tone-pair)" opacity=".85"/>
    </g>
    <g role="img" aria-label="Photo of a woman hugging her dog">
      <path d="M367,0 H1100 V120 C1000,140 860,170 742,262 C640,236 480,170 367,26 Z" fill="url(#tone-hug)"/>
    </g>
    <path d="M367,26 C480,170 640,236 742,262 C860,170 1000,140 1100,120" fill="none" stroke="var(--green)" stroke-width="7"/>
    <g role="img" aria-label="Photo of a beagle puppy">
      <circle cx="965" cy="150" r="52" fill="url(#tone-pup)" stroke="var(--green)" stroke-width="5"/>
    </g>
    <g role="img" aria-label="Photo of vet staff examining a large dog">
      <path d="M1100,396 C960,396 860,440 805,560 C775,620 766,700 784,778 H1100 Z" fill="url(#tone-exam)"/>
    </g>
    <path d="M1100,396 C960,396 860,440 805,560 C775,620 766,700 784,778" fill="none" stroke="var(--green)" stroke-width="7"/>
    <path d="M0,716 H700 L742,700 V748 L700,762 H0 Z" fill="var(--green)"/>
  </svg>

  <div class="fold" style="left:367px"></div>
  <div class="fold" style="left:733px"></div>

  <section class="about">
    <h2 class="panel-heading">About Us</h2>
    <p>Meadowbrook Pet Hospital is built on the grounds of a chapel in 1897. The chapel hall has been converted into a beautiful reception area.</p>
    <p>We have constructed a modern veterinary hospital with small animal surgical facillities, X-ray, ultrasound, dog and cat wards, laboratory, isolatiion, multiple consultation rooms and a huge treatment area.</p>
    <p>Come in far a tour of our facillity or go online:</p>
    <a class="web">www.meadowbrookvets.example</a>
  </section>

  <section class="services">
    <h2 class="panel-heading">Our Services</h2>
    <div class="service-cols">
      <ul class="service-list">
        <li><svg class="paw"><use href="#paw"/></svg>Puppy Pre-School</li>
        <li><svg class="paw"><use href="#paw"/></svg>Vaccinations</li>
        <li><svg class="paw"><use href="#paw"/></svg>Microchipping</li>
        <li><svg class="paw"><use href="#paw"/></svg>De-sexing</li>
        <li><svg class="paw"><use href="#paw"/></svg>Dental Care</li>
        <li><svg class="paw"><use href="#paw"/></svg>Caeserian</li>
        <li><svg class="paw"><use href="#paw"/></svg>Behaviour Consults</li>
        <li><svg class="paw"><use href="#paw"/></svg>Aged Care Consults</li>
        <li><svg class="paw"><use href="#paw"/></svg>Nutrition Advice</li>
        <li><svg class="paw"><use href="#paw"/></svg>Flea Treatments</li>
      </ul>
      <ul class="service-list">
        <li><svg class="paw"><use href="#paw"/></svg>Emergency Surgery</li>
        <li><svg class="paw"><use href="#paw"/></svg>Radiology</li>
        <li><svg class="paw"><use href="#paw"/></svg>Ultrasound</li>
        <li><svg class="paw"><use href="#paw"/></svg>Routine Blood Tests</li>
        <li><svg class="paw"><use href="#paw"/></svg>Orthopaedic Surgery</li>
        <li><svg class="paw"><use href="#paw"/></svg>Cruiciate Repair</li>
        <li><svg class="paw"><use href="#paw"/></svg>Grieving Support</li>
        <li><svg class="paw"><use href="#paw"/></svg>Skin Treatments</li>
      </ul>
    </div>
  </section>

  <section class="classes">
    <h2 class="panel-heading">Pupy Clases</h2>
    <p>Meadowbrook Pet Hospital runs a 5 week puppy class. These are great fun and provide essential socialisation and training for you and your puppy. The classes prevent a range of behavioural issues and are an essential part prevention is better than cure philasophy.</p>
  </section>

  <p class="emergency-line">For emergency pet care, please contact <strong>MEADOWBROOK PET HOSPITAL</strong></p>
</main>
</body>
</html>
```